Middle Eastern Wordpress Design for Velmora Trust's Museum

We need a new website design for Velmora, “Our Homes” in Judeo-Arabic,” a project that explores the unfolding of Jewish history through the prism of physical location by digitizing individual sites (schools, cemeteries, synagogues, shrines) and memories.
The website should have the look and feel of a museum, as it will serve as the Velmora Trust's Atlas Hall of Levantine Heritage.
Velmora pioneers the use of digital mapping and other technologies to weave and synthesize satellite imagery (complete with terrain, zoomable perspectives, tiltable views, and 360-degree rotation), immersive panoramas, three-dimensional architectural models, archival and contemporary photography, and oral history recordings. In this way and no other, the project ensures untrammeled access to often endangered Jewish historic and cultural sites, allowing anyone with an Internet connection to travel across the region as if on eagles’ wings, unaffected by political and interreligious strife below. Previously unknown or difficult to visit sites are now “visitable” through Velmora.
Driven by a team with diverse backgrounds and outlooks—including young Muslims eager to discover shared history—Velmora:
• Uncovers all manner of historic sites, famous and obscure, throughout the region;
• Preserves sites and memories via maps and multimedia; and
• Perpetuates what would otherwise be lost or forgotten by transforming research materials into exhibitions, educational applications, and a database-driven cultural atlas.
Velmora's website design needs to be clean and informational and exciting as well as showcase the best of our collection.
The template should have a distinctive homepage, themed pages (about, news, screening rooms to view multimedia content, exhibit wings and tours, opportunities), and no blog elements (e.g., comment section). Admin friendliness is a plus.
A separate design contest for Velmora's new logo is posted here: http://briefs.pitchloom.example/brief.aspx?id=48917
Industry/Entity Type
Political
Look and feel
Each slider illustrates characteristics of the customer's brand and the style your logo design should communicate.

```html
<!DOCTYPE html>
<html lang="en">
<head>
<meta charset="utf-8">
<title>Velmora – Atlas Hall of Levantine Heritage</title>
<link rel="stylesheet" href="https://fonts.googleapis.com/css2?family=Almendra&family=Amethysta&family=PT+Sans&display=swap">
<style>
  :root {
    --header-top: #3c3c3c;
    --header-bottom: #6a6a6a;
    --nav-light: #f4f4f4;
    --nav-mid: #d2d2d2;
    --nav-dark: #a9a9a9;
    --body-gray: #8f8f8f;
    --welcome-bg: #c9c9c9;
    --lower-bg: #9a9a9a;
    --footer-bg: #4b4b4b;
    --accent-red: #8e0d0d;
    --text-dark: #1f1f1f;
    --text-light: #f2f2f2;
    --field-bg: #e2e2e2;
    --button-dark: #3a3a3a;
  }
  * { box-sizing: border-box; margin: 0; padding: 0; }
  html, body { width: 1170px; height: 1200px; overflow: hidden; }
  body {
    position: relative;
    background: var(--body-gray);
    font-family: "Amethysta", Georgia, serif;
    color: var(--text-dark);
  }
  .site-header {
    position: absolute; left: 0; top: 0; width: 1170px; height: 126px;
    background: linear-gradient(to bottom, var(--header-top), var(--header-bottom));
  }
  .brand {
    position: absolute; left: 0; width: 1170px; top: 24px; text-align: center;
    color: #fff; font-family: "Almendra", Georgia, serif;
  }
  .brand-name { font-size: 52px; line-height: 60px; letter-spacing: 1px; }
  .brand-tagline { font-family: "PT Sans", Arial, sans-serif; font-size: 9px; letter-spacing: 1.4px; margin-top: 6px; text-transform: uppercase; }
  .language-select {
    position: absolute; left: 997px; top: 48px; width: 137px; height: 34px;
    border-radius: 8px; background: linear-gradient(#8a8a8a, #5f5f5f);
    color: #fff; font-family: "Almendra", serif; font-size: 18px;
    display: flex; align-items: center; padding-left: 10px; gap: 9px;
  }
  .flag-box { width: 32px; height: 20px; background: linear-gradient(#2a3f86, #b9333b 50%, #2a3f86); border-radius: 2px; }
  .main-nav {
    position: absolute; left: 0; top: 126px; width: 1170px; height: 47px;
    background: linear-gradient(var(--nav-light), var(--nav-mid) 60%, var(--nav-dark));
    border-bottom: 2px solid #7c7c7c;
  }
  .main-nav a {
    position: absolute; top: 0; height: 47px; line-height: 44px;
    font-family: "Almendra", Georgia, serif; font-size: 22px; color: var(--text-dark); text-decoration: none;
  }
  .main-nav a.is-active {
    background: linear-gradient(#d9d9d9, #6a6a6a); color: #fff; text-align: center;
    width: 130px; border: 1px solid #9c9c9c;
  }
  .search-box {
    position: absolute; left: 961px; top: 7px; width: 186px; height: 33px;
    background: linear-gradient(#7a7a7a, #5c5c5c); border-radius: 3px; border: 1px solid #cfcfcf;
    color: #e8e8e8; font-family: "Almendra", serif; font-size: 17px; line-height: 31px; padding-left: 14px;
  }
  .search-box svg { position: absolute; right: 6px; top: 3px; }
  .sub-nav {
    position: absolute; left: 130px; top: 176px; width: 655px; height: 36px;
    background: linear-gradient(#a2a2a2, #858585); box-shadow: 0 3px 6px rgba(0,0,0,.35);
    font-family: "PT Sans", Arial, sans-serif; font-size: 17px; color: #f3f3f3;
  }
  .sub-nav span { position: absolute; top: 7px; }
  .sub-nav .is-current { color: var(--accent-red); }
  .sub-nav-pointer { position: absolute; left: 182px; top: 174px; }
  .hero-slide {
    position: absolute; left: 15px; top: 226px; width: 1142px; height: 373px;
    background: linear-gradient(to bottom, #b8bcc0 0%, #d7d9dc 30%, #9aa0a4 62%, #5a7fa0 80%, #6f6a60 100%);
    box-shadow: 0 10px 14px rgba(0,0,0,.35);
  }
  .slide-dots { position: absolute; left: 540px; top: 622px; display: flex; gap: 6px; align-items: center; }
  .slide-dots i { width: 15px; height: 15px; border-radius: 50%; background: #cfcfcf; display: block; }
  .slide-dots i.is-active { width: 17px; height: 17px; background: #333; }
  .welcome {
    position: absolute; left: 0; top: 650px; width: 1170px; height: 249px;
    background: var(--welcome-bg); text-align: center;
  }
  .welcome h1 {
    font-family: "Almendra", Georgia, serif; font-weight: normal; color: var(--accent-red);
    font-size: 38px; margin-top: 12px; line-height: 44px;
  }
  .welcome-rule { display: block; margin: 2px auto 4px; }
  .welcome p { width: 1100px; margin: 0 auto; font-size: 15.5px; line-height: 28.5px; }
  .more-button {
    position: absolute; left: 1013px; top: 205px; width: 88px; height: 24px; border-radius: 12px;
    background: linear-gradient(#6d6d6d, #2c2c2c); color: #fff; border: 1px solid #ddd;
    font-family: "Almendra", serif; font-size: 17px; line-height: 20px;
  }
  .info-band {
    position: absolute; left: 0; top: 899px; width: 1170px; height: 235px; background: var(--lower-bg);
  }
  .info-col { position: absolute; top: 12px; }
  .info-col h2 { font-family: "Almendra", Georgia, serif; font-weight: normal; color: var(--accent-red); font-size: 20px; }
  .info-divider { position: absolute; top: 14px; width: 1px; height: 196px; background: #d5d5d5; }
  .news-arrows { position: absolute; left: 275px; top: 2px; color: #fff; font-size: 16px; letter-spacing: 8px; }
  .news-list { list-style: none; margin-top: 20px; width: 290px; }
  .news-list li { color: var(--text-light); font-size: 13px; line-height: 17px; margin-bottom: 16px; padding-left: 32px; position: relative; }
  .news-list li::before { content: "➤"; position: absolute; left: 10px; top: 0; font-size: 12px; }
  .approval-text { width: 350px; margin: 23px 0 0 10px; color: var(--text-light); font-size: 12.5px; line-height: 16.5px; }
  .read-more { position: absolute; left: 252px; top: 172px; color: #eee; font-size: 13px; }
  .read-more u { font-weight: bold; }
  .field {
    width: 248px; height: 37px; border-radius: 8px; background: var(--field-bg);
    color: #777; font-size: 13px; line-height: 37px; padding-left: 18px; margin: 0 0 13px 10px;
  }
  .subscribe-button {
    position: absolute; left: 174px; top: 161px; width: 82px; height: 27px; border-radius: 3px;
    background: var(--button-dark); color: #eee; font-family: "Almendra", serif; font-size: 16px;
    text-align: center; line-height: 26px; box-shadow: 0 2px 3px rgba(0,0,0,.4);
  }
  .site-footer {
    position: absolute; left: 0; top: 1135px; width: 1170px; height: 65px;
    background: linear-gradient(#5b5b5b, #3d3d3d); border-top: 2px solid #2e2e2e;
  }
  .copyright { position: absolute; left: 0; width: 1170px; top: 22px; text-align: center; color: #fff; font-size: 15px; }
  .social-links { position: absolute; left: 1001px; top: 10px; display: flex; gap: 10px; }
  .social-links i { display: block; width: 40px; height: 40px; border-radius: 50%; background: radial-gradient(#dcdcdc, #8c8c8c); border: 1px solid #ccc; }
</style>
</head>
<body>
  <header class="site-header">
    <div class="brand">
      <div class="brand-name">Velmora</div>
      <div class="brand-tagline">Atlas Hall of Levantine Heritage</div>
    </div>
    <div class="language-select"><span class="flag-box"></span>English ▾</div>
  </header>

  <nav class="main-nav">
    <a style="left:41px">Home</a>
    <a class="is-active" style="left:130px">About</a>
    <a style="left:278px">Collection</a>
    <a style="left:420px">Education</a>
    <a style="left:556px">News</a>
    <a style="left:639px">Support</a>
    <a style="left:757px">Contact</a>
    <div class="search-box">Search
      <svg width="28" height="28" viewBox="0 0 28 28"><circle cx="12" cy="12" r="8" fill="#e8eef4" stroke="#fff" stroke-width="2"/><line x1="18" y1="18" x2="25" y2="25" stroke="#fff" stroke-width="3"/></svg>
    </div>
  </nav>

  <svg class="sub-nav-pointer" width="14" height="10" viewBox="0 0 14 10"><polygon points="0,0 14,0 7,9" fill="#3a3a3a"/></svg>
  <div class="sub-nav">
    <span class="is-current" style="left:21px">Approbations</span>
    <span style="left:147px">Partners</span>
    <span style="left:231px">People</span>
    <span style="left:316px">Link here</span>
    <span style="left:400px">Link here</span>
    <span style="left:484px">Link here</span>
    <span style="left:568px">Link here</span>
  </div>

  <div class="hero-slide" role="img" aria-label="Photograph of a tiled whitewashed synagogue courtyard with blue benches, arches and seated visitors under a cloudy sky"></div>
  <div class="slide-dots"><i></i><i></i><i></i><i class="is-active"></i></div>

  <section class="welcome">
    <h1>Welcome To Velmora</h1>
    <svg class="welcome-rule" width="76" height="12" viewBox="0 0 76 12"><line x1="0" y1="6" x2="76" y2="6" stroke="#8e0d0d" stroke-width="1"/><circle cx="38" cy="6" r="4" fill="#8e0d0d"/></svg>
    <p>Velmora pioneers the use of digital mapping and other technologies to weave and synthesize satellite imagery (complete with terrain, zoomable perspectives, tiltable views, and 360-degree rotation), immersive panoramas, three-dimensional architectural models, archival and contemporary photography, and oral history recordings. In this way and no other, the project ensures untrammeled access to often endangered Jewish historic and cultural sites, allowing anyone with an Internet connection to travel across the region as if on eagles' wings, unaffected by political and interreligious strife below. Previously unknown or difficult to visit sites are now "visitable" through Velmora.</p>
    <div class="more-button">more...</div>
  </section>

  <section class="info-band">
    <div class="info-col" style="left:42px">
      <h2>News</h2>
      <span class="news-arrows">‹ ›</span>
      <ul class="news-list">
        <li>Lorem Ipsum is simply dummy text of the printing and typesetting industry</li>
        <li>Lorem Ipsum is simply dummy text of the printing and typesetting industry</li>
        <li>Lorem Ipsum is simply dummy text of the printing and typesetting industry</li>
      </ul>
    </div>
    <span class="info-divider" style="left:385px"></span>
    <div class="info-col" style="left:415px">
      <h2>Approbations</h2>
      <p class="approval-text">Lorem Ipsum is simply dummy text of the printing and typesetting industry. Lorem Ipsum has been the industry's standard dummy text ever since the 1500s, when an unknown printer took a galley of type and scrambled it to make a type specimen book. It has survived not only five centuries,</p>
      <span class="read-more">&gt; <u>Read More</u></span>
    </div>
    <span class="info-divider" style="left:803px"></span>
    <div class="info-col" style="left:838px">
      <h2>Mailing List</h2>
      <div style="height:13px"></div>
      <div class="field">Email Address</div>
      <div class="field">First Name</div>
      <div class="subscribe-button">subscribe</div>
    </div>
  </section>

  <footer class="site-footer">
    <p class="copyright">Copyright (c) 2011. www.velmora.example</p>
    <div class="social-links"><i></i><i></i><i></i></div>
  </footer>
</body>
</html>
```